velturi.org business card design

We need 2-sided business cards for velturi.org; one side will be printed in English (EN), the other in Spanish (ES); the information represnted will be the same.
We are a non-profit that aims to mentor and coach future leaders / visionaries. Our target markets are developing countries (Latin America, Africa, Asia) rather than the developed ("western") world. Our business model works by finding funding to mentor / coach a candidate. We provide several mentors / coaches per candidate which help translate the candidate's vision / dream into a path with objectives and steps.
We want the business cards to transmit our values, which are: innovation, learning / self-improvement, equality (i.e. free from discrimination), boldness, intelligence, thoughtfulness, culture, society, future, sustainability.
We recommend the designers work with these values to produce a bold and innovative design, which does not need to adhere to the traditional criteria for business cards. Please use fresh (modern) colours.

Target Market(s)

Visionaries and thought leaders all over the world, but initially in Latin America. We don't discriminate on age, sex, religion, race or any other difference between people

Industry/Entity Type

Leadership

Contact Information for Business Card

The business cards will contain one language (English / Spanish) per side. It would be nice to have some continuity between the front and the back (e.g. pattern, colours).
Each side will contain the company name, website (www.velturi.org) and a slogan / mantra (which will be provided and can be represented as a placeholder until such time). The other details will be Name, (Function), and contact details (email and phone number).

Font styles to use
Sans Serif

Colors

Designer to choose colors to be used in the design.

Requirements
Must have
• [Side A: ENGLISH --- COMPANY INFO]
• [Company Name] Velturi
• [Slogan / Mantra] Shape your world!
• [Website] velturi.org
• [Side A: ENGLISH --- PERSONAL INFO]
• [Name] Dan Pilcher
• [Job Title] Mentoring Coordinator
• [Phone / WhatsApp] +51 947 218 306
• [eMail] dan@velturi.org
• [Side B: SPANISH --- COMPANY INFO]
• [Company Name] Velturi
• [Slogan / Mantra] ¡Moldea tu mundo!
• [Website] velturi.org
• [Side B: SPANISH --- PERSONAL INFO]
• [Name] Daniel Pilcher
• [Job Title] Coordinador de Mentoreo
• [eMail] dan@velturi.org
• [SIDE A: ENGLISH --- Central Values]
• - Future
• - Growth
• - Leadership
• [SIDE B: SPANISH --- Central Values]
• - Futuro
• - Liderazgo
• - Crecimiento
Nice to have
• Innovative and different design. Modern and fresh. Bold and clever.
• Secondary Values (we would like represented) are:
• [SIDE A: ENGLISH --- Secondary Values]
• - Equality
• - Innovation
• - Sustainability
• [SIDE B: SPANISH --- Secondary Values]
• - Igualdad
• - Innovación
• - Sostenibilidad
Should not have
• Please note that the images I have attached to this brief are just some images that I liked while browsing for material for the website. It does not imply I want these colours or this type of design, just that I felt these images had a good feel.

```html
<!DOCTYPE html>
<html lang="en">
<head>
<meta charset="utf-8">
<title>Velturi business cards</title>
<link rel="stylesheet" href="https://fonts.googleapis.com/css2?family=Montserrat:wght@500;600&family=Open+Sans:ital,wght@0,400;0,600;0,800;1,800&display=swap">
<style>
  :root {
    --stage: #111111;
    --sun: #fbba16;
    --sun-deep: #f2a911;
    --ruby: #c8203f;
    --ruby-deep: #a8172f;
    --sky: #29a8df;
    --paper: #ffffff;
    --ink: #141414;
    --font-main: "Open Sans", Arial, sans-serif;
    --font-values: "Montserrat", Arial, sans-serif;
  }
  * { box-sizing: border-box; margin: 0; padding: 0; }
  html, body { width: 1200px; height: 1000px; overflow: hidden; }
  body { background: var(--stage); position: relative; font-family: var(--font-main); }

  .card {
    position: absolute;
    width: 700px;
    height: 400px;
    border-radius: 28px;
    overflow: hidden;
    box-shadow: 0 10px 30px rgba(0,0,0,.5);
  }
  .card--en { left: 90px; top: 70px; background: var(--sun); color: var(--ink); }
  .card--es { left: 410px; top: 530px; background: var(--ruby); color: var(--paper); }

  .card__pattern { position: absolute; inset: 0; }
  .card--en .card__pattern { background: radial-gradient(circle at 55% 50%, var(--sun-deep), var(--sun) 70%); }
  .card--es .card__pattern { background: radial-gradient(circle at 45% 50%, #b71a37, var(--ruby) 70%); }

  .values {
    position: absolute;
    width: 200px;
    height: 190px;
    display: flex;
    flex-direction: column;
    justify-content: center;
    gap: 8px;
    padding: 0 24px;
    font-family: var(--font-values);
    font-weight: 500;
    font-size: 19px;
    line-height: 1.2;
  }
  .card--en .values { background: linear-gradient(135deg, var(--ruby), var(--ruby-deep)); color: var(--paper); }
  .card--es .values { background: linear-gradient(135deg, var(--sun), var(--sun-deep)); color: var(--ruby); }
  .card--en .values--central { top: 0; right: 0; text-align: right; }
  .card--en .values--secondary { bottom: 0; left: 0; text-align: left; }
  .card--es .values--central { top: 0; left: 0; text-align: left; }
  .card--es .values--secondary { bottom: 0; right: 0; text-align: right; }

  .brand { position: absolute; line-height: 1; }
  .brand__name { font-weight: 800; font-size: 64px; letter-spacing: 1px; }
  .brand__slogan { font-weight: 600; font-size: 23px; text-transform: uppercase; margin-top: 2px; letter-spacing: .5px; }
  .card--en .brand { left: 40px; top: 32px; }
  .card--es .brand { right: 42px; top: 96px; text-align: right; }

  .contact { position: absolute; line-height: 1.2; }
  .contact__name { font-weight: 800; font-size: 25px; text-transform: uppercase; }
  .contact__role, .contact__lines { font-size: 19px; }
  .contact__web { font-weight: 800; font-style: italic; font-size: 28px; margin-top: 2px; }
  .card--en .contact { right: 40px; bottom: 30px; text-align: right; }
  .card--es .contact { left: 36px; top: 230px; }
</style>
</head>
<body>

<section class="card card--en" lang="en">
  <div class="card__pattern" role="img" aria-label="Faint background texture in warm yellow tones"></div>
  <ul class="values values--central" role="img" aria-label="Corner panel with central values" style="list-style:none">
    <li>Growth</li>
    <li>Future</li>
    <li>Leadership</li>
  </ul>
  <ul class="values values--secondary" role="img" aria-label="Corner panel with secondary values" style="list-style:none">
    <li>Sustainability</li>
    <li>Innovation</li>
    <li>Equality</li>
  </ul>
  <div class="brand">
    <div class="brand__name">VELTURI</div>
    <div class="brand__slogan">Shape your world</div>
  </div>
  <div class="contact">
    <div class="contact__name">Dan Pilcher</div>
    <div class="contact__role">Coordinator Mentoring</div>
    <div class="contact__lines">dan@velturi.org | +51 947 218 306</div>
    <div class="contact__web">www.velturi.org</div>
  </div>
</section>

<section class="card card--es" lang="es">
  <div class="card__pattern" role="img" aria-label="Textura tenue de fondo en tonos rojos"></div>
  <ul class="values values--central" role="img" aria-label="Panel de esquina con valores centrales" style="list-style:none">
    <li>Crecimiento</li>
    <li>Futuro</li>
    <li>Liderazgo</li>
  </ul>
  <ul class="values values--secondary" role="img" aria-label="Panel de esquina con valores secundarios" style="list-style:none">
    <li>Sostenibilidad</li>
    <li>Innovación</li>
    <li>Igualdad</li>
  </ul>
  <div class="brand">
    <div class="brand__name">VELTURI</div>
    <div class="brand__slogan">Moldea tu mundo</div>
  </div>
  <div class="contact">
    <div class="contact__name">Daniel Pilcher</div>
    <div class="contact__role">Coordinador de Mentoreo</div>
    <div class="contact__lines">+51 947 218 306 | dan@velturi.org</div>
    <div class="contact__web">www.velturi.org</div>
  </div>
</section>

</body>
</html>
```